New Design required for Disposable Gloves Pack

We need a new design for our range of disposable Gloves.
The brand name is "Marlow" I will attach the existing logo.

The needs to be 3 variations of the design (maybe different colours) that we can use for the different kinds of gloves: Latex Gloves, Clear Vinyl Gloves & Blue Vinyl Gloves.
Pack size is: 220x65x120mm.

Attached is a template to use showing all sides of the pack as flat. It is preferable that you supply an image of the complete folded pack as well with your design. Also attached is a PDF of our old pack design. Please use all the text on this old design for the new one.

The packs need to be easily differentiated from each other.

Target Market(s)

New Zealand Businesses, food processors & manufacturers. Medical & health care professionals

Font styles to use
Sans Serif

Requirements
Must have
• 3 variations of the same pack design to differentiate between the 3 types of gloves we offer: Latex Gloves, Clear Vinyl & Blue Vinyl Gloves.

```html
<!DOCTYPE html>
<html lang="en">
<head>
<meta charset="utf-8">
<title>Marlow Latex Gloves – Carton Dieline</title>
<link rel="stylesheet" href="https://fonts.googleapis.com/css2?family=Archivo:ital,wght@0,400;0,700;0,800;1,800&display=swap">
<style>
  :root {
    --lime: #e2e44a;
    --leaf: #6f9a3e;
    --signal-green: #0aa04a;
    --glow: #fbfde8;
    --silver: #b9bcb4;
    --ink: #2b2b2b;
    --skin: #f1d9cc;
    --paper: #ffffff;
  }
  html, body {
    margin: 0;
    width: 1200px;
    height: 1200px;
    overflow: hidden;
    background: var(--paper);
    font-family: "Archivo", Arial, sans-serif;
  }
  .dieline {
    position: absolute;
    left: 0;
    top: 345px;
    width: 1200px;
    height: 510px;
  }
  .board { fill: var(--lime); }
  .brand-curve { fill: var(--leaf); }
  .brand-name { fill: var(--paper); font-weight: 700; letter-spacing: 2px; }
  .title-band { fill: var(--signal-green); }
  .title-latex { fill: var(--paper); font-weight: 800; font-style: italic; }
  .title-gloves { fill: var(--silver); font-weight: 800; font-style: italic; stroke: #6b6d68; stroke-width: .6; }
  .size-band { fill: var(--paper); }
  .size-label { fill: var(--ink); font-weight: 800; font-style: italic; }
  .size-label--green { fill: var(--signal-green); }
  .feature-band { fill: var(--signal-green); }
  .feature-text { fill: var(--paper); }
  .hand-art { fill: var(--skin); }
  .lizard-art { fill: var(--leaf); opacity: .55; }
  .window-outline { fill: none; stroke: #f3f5d0; stroke-width: 1.2; }
  .reorder-box { fill: #f0f29a; stroke: #f7f8c4; stroke-width: .8; }
  .small-print { fill: var(--ink); font-size: 6px; }
  .contact { fill: var(--signal-green); font-size: 6px; font-weight: 700; }
</style>
</head>
<body>
<svg class="dieline" viewBox="40 880 1410 600" xmlns="http://www.w3.org/2000/svg">
  <defs>
    <radialGradient id="panel-glow" cx="0.5" cy="0.5" r="0.5">
      <stop offset="0" stop-color="var(--glow)"/>
      <stop offset="1" stop-color="var(--glow)" stop-opacity="0"/>
    </radialGradient>
  </defs>

  <!-- lid panel (printed upside down) -->
  <g class="lid-panel" transform="rotate(180 281.5 1033.5)">
    <rect class="board" x="53" y="892" width="457" height="283"/>
    <ellipse cx="290" cy="1020" rx="150" ry="150" fill="url(#panel-glow)"/>
    <path class="brand-curve" d="M360 892 H510 V1080 Q470 1010 410 990 Q370 975 360 892 Z"/>
    <text class="brand-name" x="442" y="943" font-size="17" text-anchor="middle">MARLOW</text>
    <rect class="title-band" x="117" y="922" width="150" height="18"/>
    <text class="title-latex" x="192" y="938" font-size="17" text-anchor="middle">LATEX</text>
    <text class="title-gloves" x="190" y="968" font-size="30" text-anchor="middle">GLOVES</text>
    <rect class="size-band" x="53" y="974" width="110" height="14"/>
    <text class="size-label size-label--green" x="112" y="986" font-size="13">Large</text>
    <rect class="window-outline" x="110" y="1005" width="237" height="55" rx="14"/>
    <rect class="hand-art" role="img" aria-label="Illustration of a gloved hand" x="240" y="1005" width="70" height="120" rx="20"/>
    <g class="feature-text-group" font-size="11">
      <rect class="feature-band" x="323" y="1077" width="95" height="13"/>
      <text class="feature-text" x="327" y="1087">Ambidexterous</text>
      <rect class="feature-band" x="323" y="1093" width="65" height="13"/>
      <text class="feature-text" x="327" y="1103">Single use</text>
      <rect class="feature-band" x="323" y="1109" width="90" height="13"/>
      <text class="feature-text" x="327" y="1119">Lightly powered</text>
    </g>
    <ellipse class="lizard-art" role="img" aria-label="Lizard silhouette decoration" cx="140" cy="1110" rx="60" ry="25" transform="rotate(-35 140 1110)"/>
  </g>

  <!-- front panel with bottom flap -->
  <g class="front-panel">
    <path class="board" d="M53 1175 H505 V1468 H392 V1422 H170 V1468 H53 Z"/>
    <ellipse cx="280" cy="1240" rx="150" ry="80" fill="url(#panel-glow)"/>
    <path class="brand-curve" d="M385 1175 H505 V1312 Q490 1250 440 1225 Q395 1210 385 1175 Z"/>
    <text class="brand-name" x="456" y="1214" font-size="15" text-anchor="middle">MARLOW</text>
    <rect class="title-band" x="117" y="1192" width="160" height="24"/>
    <text class="title-latex" x="200" y="1213" font-size="21" text-anchor="middle">LATEX</text>
    <text class="title-gloves" x="192" y="1248" font-size="30" text-anchor="middle">GLOVES</text>
    <rect class="size-band" x="53" y="1255" width="105" height="17"/>
    <text class="size-label" x="108" y="1268" font-size="14">Large</text>
    <rect class="hand-art" role="img" aria-label="Illustration of a gloved hand" x="292" y="1215" width="68" height="97" rx="18"/>
    <g font-size="9">
      <rect class="feature-band" x="360" y="1257" width="70" height="11"/>
      <text class="feature-text" x="363" y="1266">Ambidexterous</text>
      <rect class="feature-band" x="360" y="1270" width="55" height="11"/>
      <text class="feature-text" x="363" y="1279">Single use</text>
      <rect class="feature-band" x="360" y="1283" width="72" height="11"/>
      <text class="feature-text" x="363" y="1292">Lightly powered</text>
    </g>
  </g>

  <!-- end panel one -->
  <g class="end-panel">
    <path class="board" d="M520 1045 H737 L745 1175 V1312 L690 1360 V1468 H558 V1360 L505 1312 V1175 L510 1170 Z"/>
    <rect class="title-band" x="535" y="1233" width="110" height="14"/>
    <text class="title-latex" x="592" y="1246" font-size="14" text-anchor="middle">LATEX</text>
    <text class="title-gloves" x="588" y="1270" font-size="21" text-anchor="middle">GLOVES</text>
    <rect class="size-band" x="505" y="1274" width="60" height="11"/>
    <text class="size-label size-label--green" x="530" y="1284" font-size="10">Large</text>
    <ellipse class="lizard-art" role="img" aria-label="Lizard silhouette decoration" cx="690" cy="1212" rx="42" ry="16" transform="rotate(-30 690 1212)"/>
    <rect class="reorder-box" x="683" y="1247" width="52" height="22"/>
    <text class="small-print" x="688" y="1256">Reorder Code</text>
    <text class="contact" x="737" y="1287" text-anchor="end">0800 555 014</text>
    <text class="contact" x="737" y="1296" text-anchor="end">www.tidewellpack.co.nz</text>
  </g>

  <!-- back panel -->
  <g class="back-panel">
    <path class="board" d="M745 1170 H1190 V1312 L1080 1420 V1468 H858 V1420 L745 1312 Z"/>
    <ellipse cx="960" cy="1240" rx="150" ry="75" fill="url(#panel-glow)"/>
    <path class="brand-curve" d="M1072 1170 H1190 V1312 Q1176 1250 1128 1225 Q1082 1210 1072 1170 Z"/>
    <text class="brand-name" x="1142" y="1214" font-size="15" text-anchor="middle">MARLOW</text>
    <rect class="title-band" x="802" y="1192" width="163" height="24"/>
    <text class="title-latex" x="886" y="1213" font-size="21" text-anchor="middle">LATEX</text>
    <text class="title-gloves" x="878" y="1248" font-size="30" text-anchor="middle">GLOVES</text>
    <rect class="size-band" x="745" y="1255" width="100" height="17"/>
    <text class="size-label" x="795" y="1268" font-size="14">Large</text>
    <rect class="hand-art" role="img" aria-label="Illustration of a gloved hand" x="980" y="1215" width="66" height="95" rx="18"/>
    <g font-size="9">
      <rect class="feature-band" x="1047" y="1257" width="70" height="11"/>
      <text class="feature-text" x="1050" y="1266">Ambidexterous</text>
      <rect class="feature-band" x="1047" y="1270" width="55" height="11"/>
      <text class="feature-text" x="1050" y="1279">Single use</text>
      <rect class="feature-band" x="1047" y="1283" width="72" height="11"/>
      <text class="feature-text" x="1050" y="1292">Lightly powered</text>
    </g>
  </g>

  <!-- end panel two -->
  <g class="end-panel">
    <path class="board" d="M1200 1045 H1422 L1425 1170 H1440 V1312 L1400 1360 V1468 H1303 V1360 L1190 1312 V1170 Z"/>
    <rect class="title-band" x="1222" y="1238" width="112" height="14"/>
    <text class="title-latex" x="1280" y="1251" font-size="14" text-anchor="middle">LATEX</text>
    <text class="title-gloves" x="1274" y="1276" font-size="21" text-anchor="middle">GLOVES</text>
    <rect class="size-band" x="1190" y="1280" width="60" height="11"/>
    <text class="size-label size-label--green" x="1217" y="1290" font-size="10">Large</text>
    <ellipse class="lizard-art" role="img" aria-label="Lizard silhouette decoration" cx="1380" cy="1218" rx="42" ry="16" transform="rotate(-30 1380 1218)"/>
    <rect class="reorder-box" x="1370" y="1253" width="52" height="22"/>
    <text class="small-print" x="1375" y="1262">Reorder Code</text>
    <text class="contact" x="1424" y="1293" text-anchor="end">0800 555 014</text>
    <text class="contact" x="1424" y="1302" text-anchor="end">www.tidewellpack.co.nz</text>
  </g>
</svg>
</body>
</html>
```